Vegan Jerky company needs a label for it's pouch, and a new logo

Dear Designers - this used to be a guaranteed project, however, due to the low quality of designs I have received, I have removed the guaranteed status. However, we need this product made and we will pay for a great, high quality design that meets the requirements of our brief.

We need sticker labels that will go onto the front and back of our vegan jerky package. Our package is a zip-sealable pouch, and we will either go with black, white or brown for the color of the pouch.

We need the concept, artwork, theme and logo designed. Pls choose the colors.

There will be four flavors. These can be finished as part of another project. The flavors are: Smoked Maple, Cracked Pepper, Teriyaki Sriracha, Original.

We are Lonny and Perla's Vegan Jerky.

Our food is vegan, non GMO, straight from the farm, organic, healthy, pure, clean, made in small batches and earth friendly. We use no chemicals or artificial flavors and our product is 100% natural.

Our kitchen is yours.

Target Market(s)

Vegetarians, vegans, health conscious, ecological, intelligent, caring.

Industry/Entity Type

Food Production

Logo Text

"Lonny and Perla" and "Our Kitchen is Yours"

Colors

Designer to choose colors to be used in the design.

Requirements
Must have
• earth friendly design, classy, hipster, vegan design, shabby chic,
Nice to have
• i have no ideas really...
• We prefer black and while, with a little splash of color. The last file is an idea I had but please use your own vision.

```html
<!DOCTYPE html>
<html lang="en">
<head>
<meta charset="utf-8">
<title>Lonny and Perla's Vegan Jerky – Pouch Labels</title>
<link rel="stylesheet" href="https://fonts.googleapis.com/css2?family=Alfa+Slab+One&family=Roboto+Slab:wght@400;500&family=Oswald:wght@500;600&family=Roboto+Condensed:wght@400;700&family=Kurale&family=Montserrat:wght@500&display=swap">
<style>
  :root{
    --backdrop:#bcbfc3;
    --paper:#ffffff;
    --ink:#231f20;
    --header:#2a2a2a;
    --red:#b8151b;
    --teal:#1aa58f;
    --grey:#8d8d8d;
  }
  *{box-sizing:border-box;margin:0;padding:0}
  html,body{width:1200px;height:786px;overflow:hidden;background:var(--backdrop)}
  .canvas{position:relative;width:1200px;height:786px}
  .label{position:absolute;top:42px;width:512px;height:702px;background:var(--paper);border-radius:6px 6px 0 0;overflow:hidden;color:var(--ink)}
  .label--front{left:51px}
  .label--back{left:637px}
  .abs{position:absolute}
  .center{left:0;right:0;text-align:center}

  .header-shape{position:absolute;left:0;top:0}
  .brand{position:absolute;left:0;right:0;text-align:center;color:var(--paper);font-family:'Oswald',sans-serif;font-weight:600;text-transform:uppercase;line-height:.95}
  .brand__tagline{display:block;font-family:'Oswald',sans-serif;font-weight:500;letter-spacing:.3em;color:var(--paper);font-size:11px;margin-top:10px}

  .title-vegan{font-family:'Alfa Slab One',serif;color:var(--ink);line-height:1}
  .title-jerky{font-family:'Alfa Slab One',serif;color:var(--red);line-height:1}
  .small-batch{font-family:'Montserrat',sans-serif;font-weight:500;letter-spacing:.28em}
  .flavour{position:absolute}
  .flavour svg{position:absolute;inset:0}
  .flavour span{position:relative;display:block;text-align:center;color:var(--paper);font-family:'Roboto Slab',serif;font-weight:400}
  .claims{font-family:'Montserrat',sans-serif;font-size:10px;letter-spacing:.28em}
  .placeholder{position:absolute;border-radius:4px}
  .badge{position:absolute;border-radius:50%;background:#3a3a3a}
  .protein{position:absolute;left:212px;top:581px;width:88px;height:121px;background:var(--teal);color:var(--paper);text-align:center;font-family:'Oswald',sans-serif}
  .protein__amount{font-size:44px;line-height:1;margin-top:8px;font-weight:500}
  .protein__label{font-family:'Roboto Condensed',sans-serif;font-size:16px;margin-top:2px}
  .protein__rule{height:2px;background:var(--paper);margin:6px 8px 0}
  .protein__weight{font-family:'Roboto Slab',serif;font-size:12px;margin-top:10px}
  .footer-band{position:absolute;left:0;right:0;bottom:0;height:41px;background:var(--red)}

  .rule{position:absolute;left:65px;width:382px;height:1px;background:#555}
  .story{font-family:'Kurale',serif;font-size:12.5px;line-height:16px;text-align:center}
  .fine{font-family:'Roboto Condensed',sans-serif;font-size:10.5px;line-height:13.5px;color:#222}
  .fine b{font-size:12px}
  .mini-brand{position:absolute;left:70px;top:590px;width:73px;text-align:center;font-family:'Oswald',sans-serif;font-weight:600;color:var(--red);font-size:17px;line-height:1;text-transform:uppercase}
  .nutrition{position:absolute;left:293px;top:485px;width:145px;height:168px;border:1.5px solid var(--ink);padding:3px 5px;font-family:'Roboto Condensed',sans-serif;color:var(--ink)}
  .nutrition h3{font-family:'Oswald',sans-serif;font-weight:500;font-size:19px;line-height:1.1}
  .nutrition .serving{font-size:7.5px;line-height:9px;margin-top:3px}
  .nutrition table{width:100%;border-collapse:collapse;font-size:7.5px;margin-top:3px}
  .nutrition thead th{font-weight:400;text-align:right;padding-bottom:3px;border-bottom:4px solid var(--ink)}
  .nutrition td{border-bottom:1px solid var(--ink);padding:2.5px 0;text-align:right}
  .nutrition td:first-child{text-align:left;font-weight:700}
  .nutrition .note{font-size:7px;margin-top:2px}
</style>
</head>
<body>
<main class="canvas">

  <!-- FRONT LABEL -->
  <section class="label label--front">
    <svg class="header-shape" width="512" height="260" viewBox="0 0 512 260" role="img" aria-label="Dark header panel with geometric line pattern">
      <polygon points="0,0 512,0 512,134 256,258 0,134" fill="var(--header)"/>
    </svg>
    <div class="brand" style="top:78px;font-size:42px">Lonny and<br>Perla
      <span class="brand__tagline">Premium Quality</span>
    </div>

    <div class="abs center title-vegan" style="top:265px;font-size:84px">VEGAN</div>
    <div class="abs center title-jerky" style="top:341px;font-size:72px">JERKY</div>
    <div class="abs center small-batch" style="top:415px;font-size:16px">★ SMALL BATCH ★</div>

    <div class="flavour" style="left:94px;top:448px;width:323px;height:43px">
      <svg width="323" height="43" viewBox="0 0 323 43"><polygon points="0,0 323,0 313,21.5 323,43 0,43 10,21.5" fill="var(--red)"/></svg>
      <span style="font-size:33px;line-height:43px">SMOKED MAPLE</span>
    </div>
    <div class="abs center claims" style="top:502px">ORGANIC-HEALTHY-PURE-CLEAN</div>

    <div class="placeholder" role="img" aria-label="Small crossed arrows ornament with stars" style="left:236px;top:524px;width:40px;height:48px;background:linear-gradient(#e9d4d4,#f3eaea)"></div>
    <div class="placeholder" role="img" aria-label="Engraved illustration of a cow's head wearing a bell" style="left:392px;top:522px;width:120px;height:138px;background:linear-gradient(160deg,#e6e6e6,#b9b9b9)"></div>

    <div class="badge" role="img" aria-label="Non GMO badge" style="left:38px;top:596px;width:50px;height:50px"></div>
    <div class="badge" role="img" aria-label="Vegan badge" style="left:112px;top:596px;width:50px;height:50px"></div>

    <div class="footer-band"></div>
    <div class="protein">
      <div class="protein__amount">20g</div>
      <div class="protein__label">PROTEIN</div>
      <div class="protein__rule"></div>
      <div class="protein__weight">NET WT. 1LB</div>
    </div>
  </section>

  <!-- BACK LABEL -->
  <section class="label label--back">
    <div class="abs" role="img" aria-label="Dark header panel with geometric line pattern" style="left:0;top:0;width:512px;height:171px;background:var(--header)"></div>
    <div class="brand" style="top:58px;font-size:30px">Lonny and<br>Perla
      <span class="brand__tagline" style="font-size:8px;margin-top:6px">Premium Quality</span>
    </div>

    <div class="abs center title-vegan" style="top:182px;font-size:53px">VEGAN</div>
    <div class="abs center title-jerky" style="top:228px;font-size:46px">JERKY</div>
    <div class="abs center small-batch" style="top:273px;font-size:11px">★ SMALL BATCH ★</div>
    <div class="flavour" style="left:157px;top:295px;width:198px;height:29px">
      <svg width="198" height="29" viewBox="0 0 198 29"><polygon points="0,0 198,0 191,14.5 198,29 0,29 7,14.5" fill="var(--red)"/></svg>
      <span style="font-size:21px;line-height:29px">SMOKED MAPLE</span>
    </div>

    <div class="rule" style="top:338px"></div>
    <p class="abs story" style="left:65px;width:382px;top:346px">Made in the sunshine state with the finest Australian plant protein, handcrafted and seasoned in small batches.<br>We recommend sharing in the company of great friends over your favourite craft beer – but that's just us!</p>
    <div class="rule" style="top:418px"></div>

    <p class="abs fine" style="left:65px;width:385px;top:432px"><b>INGREDIENTS</b> :Soy Protein, Soy Sauce (Water, Wheat Gluten, Salt, Sugar, Soybean, Caramel Coloring, Sodium benzoate, A preservative),<br>MIRIN, BROWN SUGAR, CHIPOTLE CHILE, GOUND GINGER</p>
    <p class="abs fine" style="left:65px;top:488px">Allergens Contains soy and wheat flour.</p>
    <p class="abs fine" style="left:65px;width:220px;top:515px">Please store in a dry airtight container after opening and keep away from direct sunlight.</p>

    <div class="mini-brand">Lonny and<br>Perla</div>

    <div class="nutrition">
      <h3>Nutrition Facts</h3>
      <div class="serving">Serving size 25g<br>Serving per packet 3</div>
      <table>
        <thead><tr><th></th><th>Per serving</th><th>Per 100g</th></tr></thead>
        <tbody>
          <tr><td>Energy</td><td>405kJ</td><td>1215kJ</td></tr>
          <tr><td>Protein</td><td>12.6g</td><td>38.0g</td></tr>
          <tr><td>Fat</td><td>2.2g</td><td>6.7g</td></tr>
          <tr><td>Carbohydrates</td><td>6.3g</td><td>18.9g</td></tr>
          <tr><td>Sugar</td><td>5.9g</td><td>17.8g</td></tr>
          <tr><td>Sodium</td><td>276mg</td><td>830mg</td></tr>
        </tbody>
      </table>
      <div class="note">All quantities above are averages.</div>
    </div>

    <div class="footer-band"></div>
  </section>

</main>
</body>
</html>
```